Business Card Design Project

We are a commercial talent casting company, a very "now" company. We need a new business card that is both current, graphic and elegantly interesting. As we are a service business,
we need something that will attract the attention of new clients,
yet project a business that is 25 years old.

Industry/Entity Type

Business

Requirements
Must have
• 1. Logo - Nora Quillan Casting
2. Address - 47 Thornbury Street
Brooklyn, New York 11217
3. Phone - 212-738-4192
4. E-Mail - Casting@noraquillan.example

Nice to have
• Would like the card in black and white with the only accent
color being red.

```html
<!DOCTYPE html>
<html lang="en">
<head>
<meta charset="utf-8">
<title>Nora Quillan Casting – Business Card</title>
<link href="https://fonts.googleapis.com/css2?family=Michroma&family=Questrial&display=swap" rel="stylesheet">
<style>
  :root {
    --page-bg: #d9d9d9;
    --card-bg: #fafafa;
    --ink: #3a3a3a;
    --ink-soft: #555555;
    --accent: #e0262e;
    --on-accent: #ffffff;
  }
  * { margin: 0; padding: 0; box-sizing: border-box; }
  html, body {
    width: 1200px;
    height: 900px;
    overflow: hidden;
    background: var(--page-bg);
  }
  .canvas {
    position: relative;
    width: 1200px;
    height: 900px;
  }
  .business-card {
    position: absolute;
    left: 180px;
    top: 210px;
    width: 840px;
    height: 480px;
    background: var(--card-bg);
    box-shadow: 0 2px 6px rgba(0,0,0,0.12);
    overflow: hidden;
  }
  .brand-name {
    position: absolute;
    left: 58px;
    top: 92px;
    font-family: "Michroma", sans-serif;
    font-weight: 400;
    font-variant: small-caps;
    font-size: 46px;
    line-height: 58px;
    color: var(--ink);
    letter-spacing: 1px;
  }
  .accent-band {
    position: absolute;
    left: 0;
    top: 214px;
    width: 100%;
    height: 64px;
    background: var(--accent);
  }
  .brand-tagline {
    position: absolute;
    left: 58px;
    top: 2px;
    font-family: "Michroma", sans-serif;
    font-variant: small-caps;
    font-size: 46px;
    line-height: 58px;
    color: var(--on-accent);
    letter-spacing: 1px;
  }
  .contact-list {
    position: absolute;
    left: 58px;
    top: 330px;
    list-style: none;
    font-family: "Questrial", sans-serif;
    font-size: 25px;
    line-height: 31px;
    color: var(--ink-soft);
  }
  .contact-item {
    display: flex;
    align-items: flex-start;
  }
  .contact-icon {
    width: 16px;
    height: 16px;
    margin-top: 8px;
    margin-right: 24px;
    flex: none;
    fill: var(--ink-soft);
  }
</style>
</head>
<body>
<main class="canvas">
  <section class="business-card">
    <h1 class="brand-name">Nora<br>Quillan</h1>
    <div class="accent-band">
      <p class="brand-tagline">Casting</p>
    </div>
    <ul class="contact-list">
      <li class="contact-item">
        <svg class="contact-icon" viewBox="0 0 16 16" aria-hidden="true"><path d="M4 1.5l2.2 3-1.3 1.6c.8 1.8 2.2 3.3 4 4.1l1.6-1.3 3 2.2-1.2 2.6C7.5 13.6 2.3 8.4 1.4 3.6z"/></svg>
        <span>212-738-4192</span>
      </li>
      <li class="contact-item">
        <svg class="contact-icon" viewBox="0 0 16 16" aria-hidden="true"><path d="M1 3h14v10H1z M2.2 4.2L8 8.6l5.8-4.4" fill="none" stroke="#555" stroke-width="1.4"/><path d="M1 3h14L8 8.4z"/></svg>
        <span>casting@noraquillan.example</span>
      </li>
      <li class="contact-item">
        <svg class="contact-icon" viewBox="0 0 16 16" aria-hidden="true"><circle cx="8" cy="8" r="7"/><path d="M1 8h14M8 1c-3 3.5-3 10.5 0 14M8 1c3 3.5 3 10.5 0 14" fill="none" stroke="#fafafa" stroke-width="1"/></svg>
        <span>47 Thornbury Street<br>Brooklyn, New York 11217</span>
      </li>
    </ul>
  </section>
</main>
</body>
</html>
```